BrivoPeak Business Card Design Project

We are looking for a modern, clean business card design for our new company. We are a consulting firm focused on the financial services market providing management and IT consulting to banks, insurance companies, etc. Please include our company logo and company contact information from the attached file in the design. Two versions of the logo are attached, either version is acceptable. Logos are available in other file formats if needed. We would like to include the contact information for both our UK and US offices as well as the following information for each individual card holder: Name, position/title, address, phone number and e-mail address.
Updates
Project Deadline Extended
Reason: A last minute trip over seas has prevented us from finalizing the decision. A decision will be made this week. We apologize for the inconvenience.
Industry/Entity Type
Business
Contact Information for Business Card
Company logo.
Company locations and phone numbers for both the US and UK offices.
Company URL.
Cardholder Name
Cardholder Position/title
Cardholder Address
Cardholder Phone Number
Cardholder e-mail Address
Look and feel
Each slider illustrates characteristics of the customer's brand and the style your logo design should communicate.

```html
<!DOCTYPE html>
<html lang="en">
<head>
<meta charset="utf-8">
<title>BrivoPeak Partners Business Card</title>
<link href="https://fonts.googleapis.com/css2?family=Lato:wght@400;700;900&display=swap" rel="stylesheet">
<style>
  :root {
    --navy: #142b50;
    --ink: #2b2b2b;
    --grey: #6d6e71;
    --paper: #ffffff;
    --backdrop: #1c1c1c;
  }
  * { margin: 0; padding: 0; box-sizing: border-box; }
  html, body { width: 1200px; height: 965px; overflow: hidden; }
  body {
    background: var(--backdrop);
    font-family: "Lato", Arial, sans-serif;
    color: var(--ink);
    position: relative;
  }
  .card {
    position: absolute;
    left: 285px;
    width: 609px;
    height: 359px;
    background: var(--paper);
  }
  .card-front { top: 80px; }
  .card-back { top: 525px; }
  .abs { position: absolute; white-space: nowrap; }

  /* front */
  .brand-front {
    right: 21px; top: 34px;
    display: flex; align-items: center; gap: 12px;
  }
  .brand-mark { width: 40px; height: 40px; background: var(--navy); }
  .brand-name {
    font-weight: 900; color: var(--navy); font-size: 34px; letter-spacing: -0.3px;
  }
  .holder-name { left: 22px; top: 176px; font-size: 26px; color: var(--navy); font-weight: 400; }
  .holder-title { left: 22px; top: 206px; font-size: 15px; color: var(--ink); }
  .rule { left: 22px; top: 245px; width: 565px; height: 1px; background: var(--navy); }
  .contact-list { left: 22px; top: 261px; list-style: none; }
  .contact-list li {
    display: flex; align-items: center; gap: 9px;
    height: 21px; font-size: 14.5px;
  }
  .contact-list svg { width: 15px; height: 15px; fill: var(--navy); }
  .office-front { right: 21px; top: 282px; text-align: right; font-size: 14.5px; line-height: 20px; font-style: normal; }
  .foot-line { left: 0; top: 334px; width: 100%; height: 2px; background: var(--grey); }
  .foot-band { left: 0; top: 338px; width: 100%; height: 21px; background: var(--navy); }

  /* back */
  .brand-back {
    left: 33px; width: 280px; top: 104px;
    display: flex; flex-direction: column; align-items: center; gap: 30px;
  }
  .brand-back .brand-mark { width: 50px; height: 50px; }
  .brand-back .brand-name { font-size: 22px; letter-spacing: 0; }
  .site-back { left: 33px; width: 280px; top: 243px; text-align: center; font-size: 15px; font-weight: 700; color: var(--ink); }
  .divider { left: 289px; top: 109px; width: 1px; height: 142px; background: var(--ink); }
  .office { left: 309px; font-size: 15px; line-height: 20.5px; font-style: normal; }
  .office-us { top: 109px; }
  .office-uk { top: 190px; }
  .phone-label { color: var(--grey); }
  .phone-num { color: var(--navy); }
</style>
</head>
<body>
  <section class="card card-front">
    <div class="abs brand-front">
      <span class="brand-mark"></span>
      <span class="brand-name">BrivoPeak Partners</span>
    </div>
    <h1 class="abs holder-name">Dara Whitlow</h1>
    <p class="abs holder-title">President</p>
    <div class="abs rule"></div>
    <ul class="abs contact-list">
      <li>
        <svg viewBox="0 0 16 16"><path d="M1 6c0-2 3-3 7-3s7 1 7 3v1h-3V5.5C11 5 9.5 4.8 8 4.8S5 5 4 5.5V7H1zM4 8l1.5-2h5L12 8l1 5H3z"/></svg>
        000.000.0000
      </li>
      <li>
        <svg viewBox="0 0 16 16"><path d="M1 3h14v10H1zM2.5 4.5v.3L8 9l5.5-4.2v-.3zM2.5 6.5v5h11v-5L8 10.7z"/></svg>
        dwhitlow@brivopeakpartners.com
      </li>
      <li>
        <svg viewBox="0 0 16 16"><path d="M8 1a7 7 0 1 0 0 14A7 7 0 0 0 8 1zm-2 3 2 1v2l-2 1-1 3-2-3 1-3zm5 2 2 2-1 3-2 1v-3l-1-2z"/></svg>
        www.brivopeakpartners.com
      </li>
    </ul>
    <address class="abs office-front">
      418 N Cedar Hollow Rd, Suite 204-117<br>
      Lindon UT 84042, United States
    </address>
    <div class="abs foot-line"></div>
    <div class="abs foot-band"></div>
  </section>

  <section class="card card-back">
    <div class="abs brand-back">
      <span class="brand-mark"></span>
      <span class="brand-name">BrivoPeak Partners</span>
    </div>
    <p class="abs site-back">www.brivopeakpartners.com</p>
    <div class="abs divider"></div>
    <address class="abs office office-us">
      418 N Cedar Hollow Rd, Suite 204-117<br>
      Lindon UT 84042, US.<br>
      <span class="phone-label">[P]:</span> <span class="phone-num">801-555-0143</span>
    </address>
    <address class="abs office office-uk">
      14 - 16 Alder Street, London<br>
      N3 4QR&nbsp; Great Britain, UK<br>
      <span class="phone-label">[P]:</span> <span class="phone-num">+44 7700 900418</span>
    </address>
  </section>
</body>
</html>
```